continuing medical education travel company. luxury, professional, quality service

PLEASE USE THE REVISED LOGO FOR ALL CARD DESIGNS, NO SNAKE HEAD

Target Market(s)

physicians

Industry/Entity Type

Travel Industry

Contact Information for Business Card

luxury quality, spot uv, foil, rounded corners

Colors
0255a3
3176b5
cfdeed
aaaaaa
5c5c5c

Requirements
Must have
• navy, platinum, possible holographic

```html
<!DOCTYPE html>
<html lang="en">
<head>
<meta charset="utf-8">
<title>Meridian Travel – Business Cards</title>
<link href="https://fonts.googleapis.com/css2?family=Open+Sans:wght@400;600;700&display=swap" rel="stylesheet">
<style>
  :root {
    --navy: #2e3192;
    --platinum: #8a8a8c;
    --white: #ffffff;
    --backdrop: #d9d7d3;
    --card-shadow: rgba(0, 0, 0, 0.28);
  }
  * { margin: 0; padding: 0; box-sizing: border-box; }
  html, body {
    width: 1200px;
    height: 906px;
    overflow: hidden;
    background: var(--backdrop);
    font-family: "Open Sans", sans-serif;
  }
  .stage {
    position: relative;
    width: 1200px;
    height: 906px;
  }
  .card {
    position: absolute;
    width: 580px;
    height: 330px;
    border-radius: 22px;
    overflow: hidden;
    background: var(--white);
    box-shadow: 0 14px 30px var(--card-shadow);
  }
  .card--front { left: 70px; top: 70px; }
  .card--back  { left: 550px; top: 506px; }
  .card__shapes {
    position: absolute;
    inset: 0;
    width: 100%;
    height: 100%;
  }
  .wordmark {
    position: absolute;
    display: flex;
    align-items: center;
    gap: 12px;
    color: var(--navy);
    font-weight: 600;
    letter-spacing: 0.06em;
    white-space: nowrap;
    z-index: 1;
  }
  .wordmark__dot {
    width: 14px;
    height: 14px;
    border-radius: 50%;
    background: var(--navy);
    flex: none;
  }
  .card--front .wordmark { left: 70px; top: 74px; font-size: 32px; }
  .card--back .wordmark  { left: 296px; top: 92px; font-size: 23px; }
  .contact {
    position: absolute;
    left: 44px;
    top: 56px;
    color: var(--white);
  }
  .contact__name { font-size: 19px; font-weight: 700; }
  .contact__role { font-size: 13px; margin-top: 2px; }
  .contact__address {
    font-size: 13px;
    line-height: 1.3;
    margin-top: 70px;
  }
  .contact__list {
    list-style: none;
    margin-top: 14px;
    font-size: 13px;
  }
  .contact__list li {
    display: flex;
    align-items: center;
    gap: 10px;
    margin-bottom: 6px;
  }
  .contact__icon { width: 14px; height: 14px; flex: none; }
</style>
</head>
<body>
<main class="stage">

  <section class="card card--front" aria-label="Business card front">
    <svg class="card__shapes" viewBox="0 0 580 330" preserveAspectRatio="none">
      <path d="M0 260 C120 305 230 285 330 225 C420 170 500 140 580 130 L580 330 L0 330 Z" fill="var(--navy)"/>
    </svg>
    <div class="wordmark"><span class="wordmark__dot"></span>MERIDIAN TRAVEL</div>
  </section>

  <section class="card card--back" aria-label="Business card back">
    <svg class="card__shapes" viewBox="0 0 580 330" preserveAspectRatio="none">
      <rect width="580" height="330" fill="var(--navy)"/>
      <path d="M300 0 C240 80 250 170 330 230 C400 280 490 300 580 300 L580 0 Z" fill="var(--platinum)"/>
      <path d="M320 0 C265 60 260 150 340 205 C410 250 500 262 580 255 L580 0 Z" fill="var(--white)"/>
    </svg>
    <div class="wordmark"><span class="wordmark__dot"></span>MERIDIAN TRAVEL</div>
    <div class="contact">
      <p class="contact__name">Laura Bennett</p>
      <p class="contact__role">Principal</p>
      <p class="contact__address">48 Maple Ave<br>Lakeview, QC H1A 2B3</p>
      <ul class="contact__list">
        <li>
          <svg class="contact__icon" viewBox="0 0 16 16" aria-hidden="true"><circle cx="8" cy="8" r="7" fill="none" stroke="#fff" stroke-width="1.3"/><path d="M5.5 4.5l1.5 1.5-1 1c.6 1.2 1.5 2.1 2.7 2.7l1-1 1.5 1.5-1 1.2C7.8 11.2 4.8 8.2 4.6 5.6z" fill="#fff"/></svg>
          555 010 2471
        </li>
        <li>
          <svg class="contact__icon" viewBox="0 0 16 16" aria-hidden="true"><rect x="1" y="3.5" width="14" height="9" fill="#fff"/><path d="M1 3.5l7 5 7-5" fill="none" stroke="var(--navy)" stroke-width="1.2"/></svg>
          lbennett@meridiantravel.com
        </li>
        <li>
          <svg class="contact__icon" viewBox="0 0 16 16" aria-hidden="true"><circle cx="8" cy="8" r="7" fill="none" stroke="#fff" stroke-width="1.3"/><ellipse cx="8" cy="8" rx="3" ry="7" fill="none" stroke="#fff" stroke-width="1"/><path d="M1 8h14" stroke="#fff" stroke-width="1"/></svg>
          www.meridiantravel.com
        </li>
      </ul>
    </div>
  </section>

</main>
</body>
</html>
```